Calloway Holdings Website Design

We are a private equity firm based with offices based in Hong Kong, Singapore, London and Paris. Our focus is investments in property development projects, corporate ventures and loans.

We require the development of a new website and you will have to select relevant images from the likes of PixBarrel or other stock photo libraries.

We will need a design done for a PC based website and the designer selected with the favored design will also need to produce some concepts for a responsive website.

Target Market(s)

Sophisticated investors looking to invest in high return property development, businesses and mortgages.

Industry/Entity Type

Investment

Number of Pages Required

5+ page

Font styles to use
Serif
Sans Serif

Colors
0255a3
00a990

Requirements
Must have
• Clean modern feel and must portray stability and professionalism.

```html
<!DOCTYPE html>
<html lang="en">
<head>
<meta charset="utf-8">
<title>Calloway Holdings</title>
<link href="https://fonts.googleapis.com/css2?family=PT+Sans:ital,wght@0,400;0,700;1,400&display=swap" rel="stylesheet">
<style>
:root{
  --navy:#1e2357;
  --bar:#111114;
  --green:#0c6b12;
  --green-text:#0d6a14;
  --light:#ececec;
  --text:#444;
  --white:#fff;
  --footer:#050507;
}
*{margin:0;padding:0;box-sizing:border-box}
html,body{width:697px;height:1200px;overflow:hidden}
body{position:relative;font-family:"PT Sans",sans-serif;color:var(--text);background:var(--white)}
.abs{position:absolute}
.header{left:0;top:0;width:697px;height:70px;background:linear-gradient(180deg,#2c3166,#262b5c)}
.brand{left:60px;top:8px;width:80px;text-align:center;color:var(--white)}
.brand-mark{width:20px;height:20px;border-radius:50%;border:2px solid var(--white);margin:0 auto 3px}
.brand-name{font-size:8px;font-weight:700;letter-spacing:.3px;line-height:9px}
.search{left:514px;top:16px;width:118px;height:26px;border:1px solid #3d4273;font-size:7px;color:#9a9dba;padding:8px 10px}
.search svg{position:absolute;right:10px;top:8px}
.nav{left:65px;top:55px;width:567px;height:33px;background:var(--bar);display:flex;font-size:7px;font-weight:700;color:var(--white);z-index:2}
.nav span{display:flex;align-items:center;justify-content:center;height:100%}
.nav .active{background:var(--green)}
.hero{left:0;top:70px;width:697px;height:240px;
  background:
    radial-gradient(ellipse 130px 70px at 60px 240px,#2e2c2f 0%,rgba(46,44,47,.85) 50%,rgba(46,44,47,0) 100%),
    radial-gradient(ellipse 40px 200px at 190px 110px,rgba(70,62,56,.75) 0%,rgba(70,62,56,0) 100%),
    linear-gradient(180deg,#d2c3aa 0%,#c7b69b 30%,#a8957b 52%,#7d7063 68%,#5a524c 82%,#3c3a3c 100%)}
.hero-arrows{left:582px;top:286px;width:50px;height:24px;background:var(--green);display:flex;justify-content:space-around;align-items:center}
.welcome{left:0;top:310px;width:697px;height:143px;background:var(--light)}
.welcome h1{position:absolute;left:65px;top:22px;font-size:15.5px;font-weight:400;color:#222;letter-spacing:.2px}
.welcome p{position:absolute;left:65px;width:567px;font-size:7.2px;line-height:17.8px;text-align:justify;color:#555}
.funds{left:0;top:453px;width:697px;height:365px;background:radial-gradient(ellipse 260px 200px at 420px 90px,#272d66,var(--navy))}
.funds-mark{left:0;top:36px;width:697px;display:flex;justify-content:center;align-items:center;gap:6px;color:var(--white);font-size:13px;font-weight:700;letter-spacing:1px}
.funds-mark i{width:30px;height:30px;border-radius:50%;border:2px solid var(--white)}
.funds h2{position:absolute;left:0;top:91px;width:697px;text-align:center;color:var(--white);font-size:15px;font-weight:400;letter-spacing:.3px}
.card{top:131px;width:107px;height:184px;border:1px solid #c9cbe0;color:var(--white);text-align:center}
.card.active{background:var(--green)}
.card .photo{width:76px;height:76px;border-radius:50%;border:2px solid var(--white);margin:10px auto 0;box-shadow:0 0 0 2px rgba(0,0,0,.35) inset}
.card h3{font-size:7px;font-weight:700;line-height:12px;margin-top:12px}
.card p{font-size:6.4px;line-height:15px;margin:4px 8px 0;text-align:justify;text-align-last:center}
.clients{left:0;top:818px;width:697px;height:196px;background:var(--white)}
.clients h2{position:absolute;left:0;top:27px;width:697px;text-align:center;font-size:15px;font-weight:400;color:#111;letter-spacing:.3px}
.portrait{left:92px;top:57px;width:108px;height:108px;border-radius:50%;background:radial-gradient(circle at 50% 42%,#8a8a8a 0%,#a9a9a9 35%,#cfcfcf 70%,#e4e4e4 100%)}
.quote{left:261px;top:79px;width:327px;font-size:6.4px;line-height:14.5px;font-style:italic;color:#555}
.qmark{font-size:22px;color:#bbb;font-family:Georgia,serif}
.person{left:261px;top:135px;font-size:8px;font-weight:700;color:var(--green-text)}
.role{left:261px;top:149px;font-size:6.5px;color:#333}
.q-nav{left:586px;top:152px;display:flex;gap:2px}
.q-nav i{width:7px;height:7px;border-radius:50%;border:1px solid #bbb}
.partners{left:0;top:1014px;width:697px;height:101px;background:var(--light)}
.partner{top:40px;width:80px;margin-left:-40px;text-align:center;font-size:8px;font-weight:700;color:#555;display:flex;align-items:center;justify-content:center;gap:3px}
.partner i{width:8px;height:8px;border-radius:50%;background:#666}
.partner-box{left:308px;top:23px;width:70px;height:55px;border:2px solid var(--green)}
.footer{left:0;top:1115px;width:697px;height:85px;background:var(--footer)}
.footer-links{left:0;top:16px;width:697px;text-align:center;font-size:7px;color:#ddd}
.footer-links b{font-weight:400;margin:0 5px}
.copyright{left:65px;top:57px;font-size:6.5px;color:#888}
.social{left:561px;top:55px;display:flex;gap:5px}
.social i{width:15px;height:15px;border-radius:50%}
</style>
</head>
<body>
<header class="abs header">
  <div class="abs brand"><div class="brand-mark"></div><div class="brand-name">CALLOWAY<br>HOLDINGS</div></div>
  <div class="abs search">Search<svg width="7" height="7" viewBox="0 0 10 10"><circle cx="4" cy="4" r="3" fill="none" stroke="#9a9dba" stroke-width="1.5"/><line x1="6.2" y1="6.2" x2="9" y2="9" stroke="#9a9dba" stroke-width="1.5"/></svg></div>
</header>
<nav class="abs nav">
  <span class="active" style="width:69px">HOME</span>
  <span style="width:73px">SERVICES</span>
  <span style="width:105px">INVESTMENT APPROACH</span>
  <span style="width:96px">CASE STUDIES</span>
  <span style="width:114px">MISSIONS AND VALUES</span>
  <span style="width:110px">CONTACT</span>
</nav>
<div class="abs hero" role="img" aria-label="Sepia photograph of a city skyline with a glass tower along a river"></div>
<div class="abs hero-arrows">
  <svg width="8" height="10" viewBox="0 0 8 10"><path d="M6 1L2 5l4 4" stroke="#fff" stroke-width="2" fill="none"/></svg>
  <svg width="8" height="10" viewBox="0 0 8 10"><path d="M2 1l4 4-4 4" stroke="#fff" stroke-width="2" fill="none"/></svg>
</div>
<section class="abs welcome">
  <h1>WELCOME TO CALLOWAY HOLDINGS</h1>
  <p style="top:49px">Calloway Holdings is a is a boutique independent investment group that specializes in direct investments along with the provision of consulting and fund raising services to both established and emerging private companies. We are attracted to challenging assignments.</p>
  <p style="top:85px">With significant years of combined industry experience and international presence, we continually build upon our trusted relationships with principal partners to create successful and enduring investment partnerships. We trust, respect and like the people with whom we choose to work.</p>
</section>
<section class="abs funds">
  <div class="abs funds-mark"><i></i>CALLOWAY</div>
  <h2>OUR SOURCE OF FUNDS INCLUDE</h2>
  <div class="abs card" style="left:50px"><div class="photo" role="img" aria-label="Photo of hands holding a piggy bank" style="background:radial-gradient(circle at 45% 50%,#e7c9c6 0%,#a88c96 35%,#3f3f68 75%,#1f2348 100%)"></div><h3>OUR OWN<br>FUNDS</h3><p>Lorem ipsum dolor sit amet, consectetur adipiscing elit. Aenean eu tincidunt.</p></div>
  <div class="abs card active" style="left:174px"><div class="photo" role="img" aria-label="Photo of a hand presenting investor icons" style="background:radial-gradient(circle at 55% 45%,#c9d4ea 0%,#6e86bb 35%,#33416b 70%,#1c2236 100%)"></div><h3>INSTITUTIONAL<br>INVESTORS</h3><p>Sed vitae ipsum in ante ullam ibus finibus nec id mi. Sed tristique, ante.</p></div>
  <div class="abs card" style="left:298px"><div class="photo" role="img" aria-label="Photo of advisors meeting at a desk" style="background:linear-gradient(180deg,#2d4a86 0%,#4f6fa6 35%,#dfe4ee 60%,#9aa6be 100%)"></div><h3>ADVISORS AND<br>CONSULTANTS</h3><p>Nunc non imperdiet arcu, in ornare diam. Donec ven en atis urna vel.</p></div>
  <div class="abs card" style="left:422px"><div class="photo" role="img" aria-label="Photo of a pen over financial charts" style="background:radial-gradient(circle at 50% 55%,#fafafa 0%,#dde1e6 45%,#aab3be 100%)"></div><h3>STRATEGIC CORPORATE<br>INVESTORS</h3><p>Etiam vulputate, purus sed ornare rutrum, lectus sapien viverra justo, vitae tempus.</p></div>
  <div class="abs card" style="left:547px"><div class="photo" role="img" aria-label="Photo of a rising growth chart over a city" style="background:linear-gradient(180deg,#101836 0%,#28407e 45%,#5f8fd6 65%,#22325f 100%)"></div><h3>HIGH NET-WORTH<br>INDIVIDUALS</h3><p>Suspendisse a erat tristique, bibendum neque ut, sagittis mi. Cras elit lorem.</p></div>
</section>
<section class="abs clients">
  <h2>WHAT OUR CLIENTS SAY</h2>
  <div class="abs portrait" role="img" aria-label="Black and white portrait of a client"></div>
  <div class="abs qmark" style="left:240px;top:64px">&ldquo;</div>
  <p class="abs quote">Lorem Ipsum is simply dummy text of the printing and typesetting industry. Lorem Ipsum has been the industry's standard dummy text ever since the 1500s, when an unknown printer took a galley of type and scrambled it to make a type specimen book...</p>
  <div class="abs qmark" style="left:593px;top:108px">&rdquo;</div>
  <div class="abs person">Marcus Delane</div>
  <div class="abs role">Business man</div>
  <div class="abs q-nav"><i></i><i></i></div>
</section>
<section class="abs partners">
  <div class="abs partner-box"></div>
  <div class="abs partner" style="left:92px"><i></i>brightmind</div>
  <div class="abs partner" style="left:178px"><i></i>Oak Court</div>
  <div class="abs partner" style="left:254px">tinysprout</div>
  <div class="abs partner" style="left:343px">Lakeview</div>
  <div class="abs partner" style="left:430px">Red Cove Co</div>
  <div class="abs partner" style="left:526px">Verdant</div>
  <div class="abs partner" style="left:604px">Northmark</div>
</section>
<footer class="abs footer">
  <div class="abs footer-links">Home<b>|</b>Services<b>|</b>Investment Approach<b>|</b>Case Studies<b>|</b>Missions and Values<b>|</b>Contact us<b>|</b>Disclaimer<b>|</b>Privacy</div>
  <div class="abs copyright">Copyright © 2016 Calloway Holdings. All rights reserved</div>
  <div class="abs social" aria-label="Social links"><i style="background:#2f4f9a"></i><i style="background:#2a8fd0"></i><i style="background:#555"></i><i style="background:#e07b1a"></i></div>
</footer>
</body>
</html>
```